VELDRA WEBSITE

need to create a new website for VELDRA ltd
the company deals with all aspects of safety products & safety wear
we need a simple website to show
ideas can be taken from following website whose products we shall distribute in kenya
www.kwt.co.uk
www.torvik.eu
www.brimontgearhouse.com
www.gardovasupply.co.za

we need following tabs
1) home - basic company information
2) products - broken down to following categories ie gloves, head protection, ear protection, mouth protection, foot protection
3) contacts

the company profile is a reputable company dealing with all aspects of safety, HSE (health and safety equipment), and PPE (personal protective equipment)

the website should have the torvik logo for which we are an authorized distributor.
the torvi industrial range writeup can be picked from their website

Dear Designers, i shall be able to choose a final design in 2 weeks, sorry i have not been able to finalise this due to a personal reason

Target Market(s)

the buyers are all types of industry who care for their employees safety

Industry/Entity Type

Industrial

Requirements
Must have
• clean look, fresh look, user freindly
Nice to have
• clear images, quick links etc

```html
<!DOCTYPE html>
<html lang="en">
<head>
<meta charset="utf-8">
<title>Veldra Ltd. – Specialized Protective &amp; Industrial Products</title>
<link rel="stylesheet" href="https://fonts.googleapis.com/css2?family=Open+Sans:wdth,wght@75,300;75,400&family=Roboto+Condensed:wght@300;400;700&display=swap">
<style>
  :root {
    --page-bg: #eef3f8;
    --panel-bg: #ffffff;
    --nav-top: #efefef;
    --nav-bottom: #dcdcdc;
    --nav-text: #7a7a7a;
    --ink: #333333;
    --body-text: #555555;
    --muted: #8a8a8a;
    --accent: #f6ae2d;
    --brand-navy: #1d3a4a;
    --tab-grey: #6d6d6d;
    --hero-sky: #3b6ea8;
    --hero-dusk: #1f3350;
    --hero-glow: #8a6a4a;
  }
  * { margin: 0; padding: 0; box-sizing: border-box; }
  html, body { width: 936px; height: 1200px; overflow: hidden; }
  body {
    position: relative;
    background: var(--page-bg);
    font-family: "Roboto Condensed", "Arial Narrow", sans-serif;
    color: var(--body-text);
  }
  .site {
    position: absolute; left: 37px; top: 0; width: 861px; height: 1057px;
    background: var(--panel-bg);
    box-shadow: 0 4px 14px rgba(0,0,0,0.25);
  }
  .brand {
    position: absolute; left: 27px; top: 34px;
    display: flex; align-items: center; gap: 10px;
  }
  .brand-mark { width: 26px; height: 26px; background: var(--accent); }
  .brand-name {
    font-family: "Roboto Condensed", sans-serif; font-weight: 700;
    font-size: 44px; letter-spacing: -1px; color: var(--brand-navy); line-height: 1;
  }
  .contact-info {
    position: absolute; right: 27px; top: 28px;
    text-align: right; font-size: 12.5px; line-height: 25px; color: var(--muted);
  }
  .contact-info b { font-weight: 400; color: var(--ink); margin-right: 6px; }
  .contact-info svg { vertical-align: -2px; margin-right: 2px; }
  .main-nav {
    position: absolute; left: 0; top: 145px; width: 861px; height: 42px;
    background: linear-gradient(var(--nav-top), var(--nav-bottom));
    display: flex; justify-content: center; align-items: center; gap: 28px;
    font-size: 13px; letter-spacing: 0.5px; color: var(--nav-text);
  }
  .hero {
    position: absolute; left: 0; top: 187px; width: 861px; height: 491px;
    background: linear-gradient(180deg, var(--hero-sky) 0%, var(--hero-dusk) 45%, var(--hero-glow) 80%, #3a3026 100%);
  }
  .slider-tabs {
    position: absolute; left: 0; top: 678px; width: 861px; height: 16px;
    display: flex; gap: 1px; background: #8a8a8a;
  }
  .slider-tabs span { flex: 1; background: var(--tab-grey); }
  .slider-tabs span.active { background: var(--accent); }
  .feature {
    position: absolute; top: 732px; width: 196px;
  }
  .feature h2 {
    font-family: "Open Sans", sans-serif; font-stretch: 75%; font-weight: 300;
    font-size: 29px; color: var(--ink); text-align: center; line-height: 1.1;
    height: 48px;
  }
  .feature-media {
    width: 105px; height: 87px; margin: 0 auto; display: flex; align-items: center; justify-content: center;
  }
  .feature-media.photo-head { background: linear-gradient(135deg, #c9d65a, #3a6fb5 60%, #e05a3a); border: 1px solid #ccc; }
  .feature-media.photo-eye { background: linear-gradient(135deg, #f4c430, #f08a1c 60%, #d0641a); }
  .partner-name { font-family: "Roboto Condensed", sans-serif; font-weight: 700; font-size: 40px; color: #1a5aa8; }
  .feature-media .brand-name { font-size: 34px; }
  .feature p { margin-top: 16px; font-size: 13px; line-height: 25px; letter-spacing: -0.3px; }
  .feature a { display: block; font-size: 13px; color: var(--accent); text-decoration: none; line-height: 24px; }
  .footer {
    position: absolute; left: 0; top: 1157px; width: 936px; text-align: center;
    font-size: 13px; color: var(--body-text); letter-spacing: -0.3px;
  }
</style>
</head>
<body>
  <div class="site">
    <header>
      <div class="brand"><span class="brand-mark"></span><span class="brand-name">VELDRA</span></div>
      <div class="contact-info">
        <div><svg width="12" height="12" viewBox="0 0 12 12"><path d="M3 1l2 3-1 1c.6 1.4 1.6 2.4 3 3l1-1 3 2-1 2C5 11 1 7 1 2z" fill="#555"/></svg><b>Toll Free :</b>0000-000-0000</div>
        <div><svg width="12" height="12" viewBox="0 0 12 12"><path d="M3 1l2 3-1 1c.6 1.4 1.6 2.4 3 3l1-1 3 2-1 2C5 11 1 7 1 2z" fill="#555"/></svg><b>Phone :</b>000-000-000</div>
        <div><svg width="13" height="10" viewBox="0 0 13 10"><rect x="0.5" y="0.5" width="12" height="9" fill="none" stroke="#555"/><path d="M.5 .5l6 5 6-5" fill="none" stroke="#555"/></svg><b>Email :</b>info@veldra.com</div>
      </div>
    </header>
    <nav class="main-nav"><span>HOME</span><span>ABOUT US</span><span>PRODUCTS</span><span>CONTACT</span></nav>
    <div class="hero" role="img" aria-label="Evening city skyline with a tall round office tower lit against a blue dusk sky"></div>
    <div class="slider-tabs"><span></span><span></span><span></span><span class="active"></span></div>

    <section class="feature" style="left:20px">
      <h2>Distributors</h2>
      <div class="feature-media"><span class="partner-name">Torvik</span></div>
      <p>Maecenas id lorem nec antein nec venenatis condimentum. Curabitur commodo ipsum nibh iaculis.</p>
      <a href="#">Read More...</a>
    </section>
    <section class="feature" style="left:230px">
      <h2>Head Safety</h2>
      <div class="feature-media photo-head" role="img" aria-label="Assorted hard hats, ear muffs and safety glasses"></div>
      <p>Quisque elit purus id into Vivamus ipsumion dui, lobortis facilisis then placerat in, venenatis vel.</p>
      <a href="#">Read more</a>
    </section>
    <section class="feature" style="left:439px">
      <h2>Eye &amp; Ear Safety</h2>
      <div class="feature-media photo-eye" role="img" aria-label="Safety first banner with hard hat and protective gear"></div>
      <p>Aenean egestas tristique justo, nec commodo orci Maecenas ultriciesn enim non luctus malesuada.</p>
      <a href="#">Read more</a>
    </section>
    <section class="feature" style="left:648px">
      <h2>Veldra Ltd.</h2>
      <div class="feature-media"><span class="brand-name">VELDRA</span></div>
      <p style="margin-top:6px">Phasellus quam ipsum rutrum then aliquam rutrum ligula rictu lorem risus Sed vulputate tincidunt.</p>
      <a href="#">Read more</a>
    </section>
  </div>
  <footer class="footer">© Copyright 2014 : Veldra Ltd. : All Rights Reserved</footer>
</body>
</html>
```